Business Cards

I'd like help creating business cards with the full logo "Veltrona Capital Partners" on the back of the card (navy background with white writing), and abbreviated logo "VCP" on the front. Would like to list name, title, phone number, email, and website listed on front of card. Would like to keep very simple. Front font Arial or similar.

```html
<!DOCTYPE html>
<html lang="en">
<head>
<meta charset="UTF-8">
<title>Veltrona Capital Partners — Business Cards</title>
<link rel="stylesheet" href="https://fonts.googleapis.com/css2?family=Arimo:wght@400;700&family=Montserrat:wght@500;700&display=swap">
<style>
  :root {
    --navy: #1c3a6e;
    --white: #ffffff;
    --paper: #f7f7f7;
    --ink-grey: #555a62;
    --backdrop: #e9e9ec;
  }
  * { box-sizing: border-box; margin: 0; padding: 0; }
  html, body { width: 1200px; height: 960px; overflow: hidden; }
  body {
    background: var(--backdrop);
    position: relative;
    font-family: "Arimo", Arial, sans-serif;
  }
  .card {
    position: absolute;
    width: 560px;
    height: 320px;
    border-radius: 20px;
    box-shadow: 0 10px 26px rgba(0,0,0,0.22);
  }
  /* back of card */
  .card-back {
    left: 360px;
    top: 80px;
    background: var(--navy);
    color: var(--white);
    display: flex;
    flex-direction: column;
    align-items: center;
    justify-content: center;
  }
  .brand-name {
    font-family: "Montserrat", sans-serif;
    font-weight: 700;
    font-size: 44px;
    letter-spacing: 3px;
    line-height: 1;
    text-transform: uppercase;
  }
  .brand-sub {
    font-family: "Montserrat", sans-serif;
    font-weight: 700;
    font-size: 17px;
    letter-spacing: 9px;
    margin-top: 12px;
    text-transform: uppercase;
  }
  .back-web {
    position: absolute;
    bottom: 26px;
    width: 100%;
    text-align: center;
    font-size: 15px;
    letter-spacing: 4px;
  }
  /* front of card */
  .card-front {
    left: 240px;
    top: 440px;
    background: var(--navy);
    padding: 14px;
  }
  .front-inner {
    position: relative;
    width: 100%;
    height: 100%;
    background: var(--paper);
    border-radius: 8px;
  }
  .person { position: absolute; left: 26px; top: 20px; }
  .person-name { color: var(--navy); font-weight: 700; font-size: 22px; }
  .person-title { color: var(--ink-grey); font-size: 14px; margin-top: 1px; }
  .contact-list {
    position: absolute;
    left: 20px;
    bottom: 26px;
    list-style: none;
    color: var(--navy);
    font-size: 17px;
    line-height: 22px;
  }
  .contact-list li { display: flex; align-items: center; gap: 10px; }
  .contact-list svg { width: 13px; height: 13px; fill: var(--navy); }
  .front-mark {
    position: absolute;
    right: 28px;
    bottom: 26px;
    display: flex;
    align-items: center;
    gap: 10px;
    color: var(--navy);
    font-family: "Arimo", Arial, sans-serif;
    font-weight: 700;
    font-size: 62px;
    line-height: 1;
  }
  .front-mark .mark-square { width: 16px; height: 16px; background: var(--navy); }
</style>
</head>
<body>
  <section class="card card-back">
    <div class="brand-name">Veltrona</div>
    <div class="brand-sub">Capital Partners</div>
    <div class="back-web">www.VCP.com</div>
  </section>

  <section class="card card-front">
    <div class="front-inner">
      <div class="person">
        <div class="person-name">Daniel Carver</div>
        <div class="person-title">President</div>
      </div>
      <ul class="contact-list">
        <li>
          <svg viewBox="0 0 16 16" aria-hidden="true"><path d="M3.6 1.5l2.3 0 1 3.4-1.6 1.2a8 8 0 0 0 4.6 4.6l1.2-1.6 3.4 1v2.3c0 .9-.8 1.6-1.7 1.6C6.8 14 2 9.2 2 3.2c0-.9.7-1.7 1.6-1.7z"/></svg>
          (555) 8473-2190
        </li>
        <li>
          <svg viewBox="0 0 16 16" aria-hidden="true"><path d="M1 3h14v10H1z M2.2 4.2v.4L8 8.6l5.8-4v-.4z" fill-rule="evenodd"/></svg>
          name@VCP.com
        </li>
        <li>
          <svg viewBox="0 0 16 16" aria-hidden="true"><circle cx="8" cy="8" r="7"/></svg>
          www.VCP.com
        </li>
      </ul>
      <div class="front-mark">
        <span class="mark-square"></span>
        <span>VCP</span>
      </div>
    </div>
  </section>
</body>
</html>
```